Investment Advisor E-Newsletter Banner Design

I need a banner designed for an email newsletter that will be sent monthly to clients and prospects. We want to see designs that are elegant and use our logo well. The banner should be 922x150px and should go well with the www.bltvorna.com website. Should include Logo and email and phone number.

Target Market(s)

High net worth investors

Number of Pages Required

1 page

Requirements
Must have
• logo, place for email (info@bltvorna.com) and phone number (555-297-6184), colors and design that work well with www.bltvorna.com website

```html
<!DOCTYPE html>
<html lang="en">
<head>
<meta charset="utf-8">
<title>Vorna Capital Newsletter Banner</title>
<link rel="stylesheet" href="https://fonts.googleapis.com/css2?family=Arimo:wght@400;700&display=swap">
<style>
  :root {
    --brand-navy: #1d2a7a;
    --sky-blue: #2a3fa8;
    --sky-deep: #1a237e;
    --swoosh-black: #121212;
    --photo-haze: #eceff3;
    --paper: #ffffff;
    --ink: #2a2a2a;
    --rule: #8a8f99;
  }
  html, body {
    margin: 0;
    padding: 0;
    overflow: hidden;
    background: var(--paper);
  }
  .banner {
    position: relative;
    width: 1200px;
    height: 195px;
    overflow: hidden;
    background: var(--paper);
    font-family: "Arimo", Arial, sans-serif;
  }
  .banner__art {
    position: absolute;
    inset: 0;
    width: 1200px;
    height: 195px;
  }
  .brand {
    position: absolute;
    left: 735px;
    top: 100px;
    display: flex;
    align-items: center;
    gap: 14px;
    color: var(--brand-navy);
  }
  .brand__dot {
    width: 44px;
    height: 44px;
    border-radius: 50%;
    background: var(--brand-navy);
    flex: none;
  }
  .brand__name {
    margin: 0;
    font-weight: 400;
    line-height: 1;
  }
  .brand__title {
    display: block;
    font-size: 30px;
    letter-spacing: 0.2px;
  }
  .brand__sub {
    display: block;
    margin-top: 7px;
    font-size: 13px;
  }
  .contact {
    position: absolute;
    left: 996px;
    top: 100px;
    height: 72px;
    padding-left: 18px;
    border-left: 2px solid var(--rule);
    list-style: none;
    margin: 0;
    display: flex;
    flex-direction: column;
    justify-content: space-between;
    font-size: 15.5px;
    color: var(--ink);
  }
  .contact__label {
    font-weight: 700;
  }
</style>
</head>
<body>
  <header class="banner">
    <svg class="banner__art" viewBox="0 0 922 150" preserveAspectRatio="none" aria-hidden="false">
      <defs>
        <linearGradient id="haze" x1="0" y1="0" x2="1" y2="0">
          <stop offset="0" stop-color="#f3f4f7"/>
          <stop offset="0.5" stop-color="var(--photo-haze)"/>
          <stop offset="1" stop-color="#fafafa"/>
        </linearGradient>
        <linearGradient id="sky" x1="0" y1="0" x2="1" y2="1">
          <stop offset="0" stop-color="var(--sky-deep)"/>
          <stop offset="1" stop-color="var(--sky-blue)"/>
        </linearGradient>
      </defs>
      <rect class="team-photo" x="200" y="0" width="722" height="150" fill="url(#haze)"
            role="img" aria-label="Faded photograph of a business team meeting in an office"/>
      <path class="swoosh" d="M0,0 H360 C300,40 170,100 60,150 H0 Z" fill="var(--swoosh-black)"/>
      <path class="skyline-photo" d="M0,0 H360 C250,10 120,40 0,85 Z" fill="url(#sky)"
            role="img" aria-label="Blue-toned photograph of a city skyline"/>
    </svg>

    <div class="brand">
      <span class="brand__dot"></span>
      <p class="brand__name">
        <span class="brand__title">Vorna Capital</span>
        <span class="brand__sub">Advisory &amp; Research, Inc.</span>
      </p>
    </div>

    <ul class="contact">
      <li><span class="contact__label">P:</span> 555-297-6184</li>
      <li><span class="contact__label">F:</span> 555-318-0427</li>
      <li><span class="contact__label">E:</span> info@bltvorna.com</li>
    </ul>
  </header>
</body>
</html>
```